item 1. 8.5x11 1-side flyer design
item 2. 18x24 1-side poster design (also wants at 8.5x11)
item 3. 11x8.5 2-side brochure
design with Larkfield Healthcare brand standards similar to the job you did under 360565
see all attachments

```html
<!DOCTYPE html>
<html lang="en">
<head>
<meta charset="utf-8">
<title>Congenital Syphilis Flyer – Larkfield Healthcare</title>
<link href="https://fonts.googleapis.com/css2?family=Figtree:wght@400;500;600;700;800&display=swap" rel="stylesheet">
<style>
  :root{
    --navy:#223a48;
    --sage:#80a48f;
    --taupe:#aaa09a;
    --teal:#6fae9f;
    --paper:#ffffff;
    --ground:#eceff3;
    --ink:#2b3338;
  }
  *{box-sizing:border-box;margin:0;padding:0}
  html,body{width:996px;height:1200px;overflow:hidden;background:var(--ground)}
  body{font-family:"Figtree",sans-serif;color:var(--ink);position:relative}
  .flyer{position:absolute;left:35px;top:0;width:927px;height:1200px;background:var(--paper);overflow:hidden}
  .abs{position:absolute}

  .stethoscope-art{left:253px;top:70px;width:380px;height:386px;border-radius:50%;
    background:radial-gradient(ellipse at center,rgba(111,174,159,.22) 0%,rgba(111,174,159,.08) 45%,rgba(255,255,255,0) 70%)}

  .headline-tag{left:47px;top:217px;width:395px;height:116px;background:var(--taupe);transform:rotate(-2deg);transform-origin:left top}
  .headline-tag span{position:absolute;left:36px;top:2px;font-size:88px;font-weight:600;color:#fff;line-height:1.15;letter-spacing:-2px}
  .headline-lead{left:116px;top:64px;font-size:53px;font-weight:400;color:var(--sage);line-height:1;letter-spacing:-.5px}
  .headline-main{left:44px;top:108px;font-size:99px;font-weight:700;color:var(--navy);line-height:1;letter-spacing:-3px}

  .brand{left:650px;top:118px;width:240px;text-align:center;color:var(--navy)}
  .brand-dot{width:70px;height:70px;border-radius:50%;background:var(--navy);margin:0 auto 40px}
  .brand-name{font-size:46px;font-weight:500;line-height:38px;letter-spacing:-1px}

  .means-lead{left:46px;top:440px;font-size:32px;font-weight:400;color:var(--navy);line-height:1}
  .means-main{left:45px;top:478px;font-size:54px;font-weight:700;color:var(--navy);line-height:1;letter-spacing:-1.5px}

  .ornament{background:var(--taupe);border-radius:50%}

  .info-card{font-size:19.5px;line-height:25.8px;color:#fff;font-weight:400}
  .info-card.sage{left:46px;top:558px;width:362px;height:188px;background:var(--sage);padding:27px 24px 0 31px}
  .info-card.navy{left:95px;top:734px;width:363px;height:187px;background:var(--navy);padding:26px 20px 0 31px}

  .closing{left:46px;top:973px;width:410px;font-size:19.5px;line-height:25.8px;color:var(--ink)}
  .closing p+p{margin-top:12px}
  .closing strong{font-weight:700;color:var(--navy)}

  .contact-box{left:465px;top:968px;width:409px;height:181px;border:1.5px solid var(--taupe)}
  .contact-title{left:493px;top:1137px;transform:rotate(-90deg);transform-origin:left top;font-size:26px;font-weight:700;color:var(--navy);white-space:nowrap;line-height:1}
  .contact-list{left:549px;top:1018px;list-style:none;font-size:19px;color:var(--navy);line-height:22px}
  .contact-list li{display:flex;align-items:flex-start;gap:8px;margin-bottom:6px}
  .contact-list svg{flex:none;margin-top:3px}

  .photo-frame{left:528px;top:443px;width:362px;height:550px;border:1.5px solid var(--navy);border-radius:8px}
  .photo{left:483px;top:417px;width:405px;height:576px;border-radius:140px 140px 8px 8px;
    background:linear-gradient(160deg,#5a4437 0%,#8d7666 28%,#d9cdc3 55%,#efe9e2 80%,#e3dbd2 100%)}
  .ring{left:0;top:0;width:927px;height:1200px;pointer-events:none}
</style>
</head>
<body>
<main class="flyer">
  <div class="abs stethoscope-art" role="img" aria-label="Teal stethoscope lying across the headline"></div>

  <div class="abs headline-tag"><span>Syphilis?</span></div>
  <div class="abs headline-lead">What is</div>
  <div class="abs headline-main">Congenital</div>

  <div class="abs brand">
    <div class="brand-dot"></div>
    <div class="brand-name">Larkfield<br>Healthcare</div>
  </div>

  <div class="abs means-lead">Congenital Means</div>
  <div class="abs means-main">FROM BIRTH</div>

  <div class="abs ornament" style="left:400px;top:492px;width:40px;height:34px" role="img" aria-label="Heart ornament"></div>
  <div class="abs ornament" style="left:436px;top:532px;width:21px;height:19px" role="img" aria-label="Heart ornament"></div>
  <div class="abs ornament" style="left:35px;top:782px;width:38px;height:38px" role="img" aria-label="Heart ornament"></div>
  <div class="abs ornament" style="left:55px;top:836px;width:20px;height:23px" role="img" aria-label="Heart ornament"></div>

  <div class="abs info-card sage">When a pregnant person is infected with syphilis it can be passed on to the newborn unless the mother gets treatment before the baby is born.</div>
  <div class="abs info-card navy">You will have lots of blood tests taken during your pregnancy. One of these tests is to check for syphilis. We need to know so that we can treat you.</div>

  <div class="abs closing">
    <p>Congenital syphilis is <strong>deadly to a newborn.</strong><br>It is important to get treatment to save<br>your baby!</p>
    <p>Attending all of your <strong>scheduled prenatal<br>appointments</strong> is the best thing you can do<br>for your health and for your baby.</p>
  </div>

  <div class="abs contact-box"></div>
  <div class="abs contact-title">Reach Us!</div>
  <ul class="abs contact-list">
    <li><svg width="14" height="14" viewBox="0 0 24 24"><path fill="#80a48f" d="M6.6 10.8a15 15 0 0 0 6.6 6.6l2.2-2.2a1 1 0 0 1 1-.25 11.4 11.4 0 0 0 3.6.57 1 1 0 0 1 1 1V20a1 1 0 0 1-1 1A17 17 0 0 1 3 4a1 1 0 0 1 1-1h3.5a1 1 0 0 1 1 1c0 1.25.2 2.45.57 3.57a1 1 0 0 1-.25 1z"/></svg>(555) 014-2290</li>
    <li><svg width="14" height="14" viewBox="0 0 24 24"><path fill="#80a48f" d="M5 3l14 8-6 1.5 4 7-2.5 1.5-4-7L6 18z"/></svg>larkfieldhealthcare.net</li>
    <li><svg width="14" height="16" viewBox="0 0 24 28"><path fill="#80a48f" d="M12 1a9 9 0 0 0-9 9c0 6.8 9 17 9 17s9-10.2 9-17a9 9 0 0 0-9-9zm0 12.5A3.5 3.5 0 1 1 12 6.5a3.5 3.5 0 0 1 0 7z"/></svg><span>1480 E. Alder Ridge Rd<br>Fernwood, AZ 85000</span></li>
  </ul>

  <div class="abs photo-frame"></div>
  <div class="abs photo" role="img" aria-label="Photo of a mother holding her newborn baby close"></div>
  <svg class="abs ring" viewBox="0 0 927 1200" aria-hidden="true">
    <path d="M700 433 A267 267 0 1 1 537 876" fill="none" stroke="var(--sage)" stroke-width="17"/>
  </svg>
</main>
</body>
</html>
```